Rollers & Glides.com

Vertical Business Card with focus on branding with our icon. Information on card will be logo, persons name, position, phone number, email address and website. Use the the name Marcus Delby, position President, phone number 480.315.7792, email Marcus@rollersandglides-example.com, website www.rollersandglides-example.com.

```html
<!DOCTYPE html>
<html lang="en">
<head>
<meta charset="UTF-8">
<title>Rollers &amp; Glides.com — Business Card</title>
<link href="https://fonts.googleapis.com/css2?family=Montserrat:wght@400;700&family=Roboto:wght@400;500&display=swap" rel="stylesheet">
<style>
  :root {
    --backdrop: #bcbdbf;
    --card: #ffffff;
    --brand-blue: #1b4a9c;
    --text-gray: #555658;
    --title-gray: #6d6e70;
  }
  * { margin: 0; padding: 0; box-sizing: border-box; }
  html, body {
    width: 1200px;
    height: 1200px;
    overflow: hidden;
    background: var(--backdrop);
  }
  .stage {
    position: relative;
    width: 1200px;
    height: 1200px;
  }
  .card {
    position: absolute;
    top: 267px;
    width: 380px;
    height: 666px;
    background: var(--card);
    text-align: center;
  }
  .card--left { left: 196px; }
  .card--right { left: 624px; }

  .card__name {
    position: absolute;
    top: 337px;
    top: 337px;
    left: 0; right: 0;
    top: 70px;
    font-family: "Montserrat", sans-serif;
    font-weight: 700;
    font-size: 29px;
    letter-spacing: 0.5px;
    color: var(--brand-blue);
    line-height: 1;
  }
  .card__title {
    position: absolute;
    left: 0; right: 0;
    top: 107px;
    font-family: "Roboto", sans-serif;
    font-weight: 500;
    font-size: 25px;
    color: var(--title-gray);
    line-height: 1;
  }
  .brand {
    position: absolute;
    left: 0; right: 0;
    top: 268px;
    display: flex;
    flex-direction: column;
    align-items: center;
    gap: 18px;
  }
  .brand__dot {
    width: 64px;
    height: 64px;
    border-radius: 50%;
    background: var(--brand-blue);
  }
  .brand__name {
    font-family: "Montserrat", sans-serif;
    font-weight: 700;
    font-size: 27px;
    color: var(--brand-blue);
    line-height: 1;
  }
  .contact-icons {
    position: absolute;
    left: 0; right: 0;
    top: 483px;
    display: flex;
    justify-content: center;
    gap: 6px;
  }
  .contact-icons svg { width: 23px; height: 23px; display: block; }
  .contact {
    position: absolute;
    left: 0; right: 0;
    font-family: "Montserrat", sans-serif;
    font-weight: 400;
    color: var(--text-gray);
    line-height: 1;
    white-space: nowrap;
  }
  .contact--phone { top: 520px; font-size: 21px; }
  .contact--email { top: 550px; font-size: 16px; }
  .contact--web { top: 573px; font-size: 16px; }
</style>
</head>
<body>
<div class="stage">
  <section class="card card--left">
    <h1 class="card__name">MARCUS DELBY</h1>
    <p class="card__title">President</p>
    <div class="brand">
      <span class="brand__dot"></span>
      <span class="brand__name">Rollers &amp; Glides.com</span>
    </div>
    <div class="contact-icons" aria-hidden="true">
      <svg viewBox="0 0 24 24"><path fill="#1b4a9c" d="M3 8c0-2 4-4 9-4s9 2 9 4v2h-5V8H8v2H3z"/><path fill="#1b4a9c" d="M7 11h10l2 9H5z"/><g fill="#fff"><rect x="9" y="13" width="2" height="2"/><rect x="13" y="13" width="2" height="2"/><rect x="9" y="16" width="2" height="2"/><rect x="13" y="16" width="2" height="2"/></g></svg>
      <svg viewBox="0 0 24 24"><path fill="#1b4a9c" d="M2 10l10-7 10 7v11H2z"/><path fill="#fff" d="M4 11l8 6 8-6v1.5l-8 6-8-6z"/></svg>
      <svg viewBox="0 0 24 24"><circle cx="12" cy="12" r="10" fill="#1b4a9c"/><path fill="#fff" d="M7 6c2 0 3 2 5 2s1 3-1 3-2 3-4 2-1-4-2-5zm8 6c2 0 4 1 3 3s-2 4-4 4 0-3-1-4 0-3 2-3z"/></svg>
    </div>
    <p class="contact contact--phone">480.315.7792</p>
    <p class="contact contact--email">Marcus@rollersandglides-example.com</p>
    <p class="contact contact--web">www.rollersandglides-example.com</p>
  </section>

  <section class="card card--right">
    <h1 class="card__name">MARCUS DELBY</h1>
    <p class="card__title">President</p>
    <div class="brand">
      <span class="brand__dot"></span>
      <span class="brand__name">Rollers &amp; Glides.com</span>
    </div>
    <div class="contact-icons" aria-hidden="true">
      <svg viewBox="0 0 24 24"><path fill="#1b4a9c" d="M3 8c0-2 4-4 9-4s9 2 9 4v2h-5V8H8v2H3z"/><path fill="#1b4a9c" d="M7 11h10l2 9H5z"/><g fill="#fff"><rect x="9" y="13" width="2" height="2"/><rect x="13" y="13" width="2" height="2"/><rect x="9" y="16" width="2" height="2"/><rect x="13" y="16" width="2" height="2"/></g></svg>
      <svg viewBox="0 0 24 24"><path fill="#1b4a9c" d="M2 10l10-7 10 7v11H2z"/><path fill="#fff" d="M4 11l8 6 8-6v1.5l-8 6-8-6z"/></svg>
      <svg viewBox="0 0 24 24"><circle cx="12" cy="12" r="10" fill="#1b4a9c"/><path fill="#fff" d="M7 6c2 0 3 2 5 2s1 3-1 3-2 3-4 2-1-4-2-5zm8 6c2 0 4 1 3 3s-2 4-4 4 0-3-1-4 0-3 2-3z"/></svg>
    </div>
    <p class="contact contact--phone">480.315.7792</p>
    <p class="contact contact--email">Marcus@rollersandglides-example.com</p>
    <p class="contact contact--web">www.rollersandglides-example.com</p>
  </section>
</div>
</body>
</html>
```